Educational -After School Tutoring

This is a flyer given out to parents from school inside their weekly flyer This flyer should bring a good first impression and carry information about my Tutoring center ( Brightpath Learning) We like this flyer to represent my Academy and the programs that we offer. Also, the flyer should tell how we differentiate from other business
Also, it should give a map or location of my business and the contact information

you may able to get more information from my website brightpathlearnga.example

Target Market(s)

Educational Community ( Parents, Teachers, Students )

Industry/Entity Type

Education

Font styles to use
Serif
Script

Requirements
Must have
• A Picture with students infer the message of tutoring
Nice to have
• teacher explaining or student observing

```html
<!DOCTYPE html>
<html lang="en">
<head>
<meta charset="utf-8">
<title>Brightpath Learning – Georgia Milestones Test Prep</title>
<link rel="stylesheet" href="https://fonts.googleapis.com/css2?family=Open+Sans:wght@400;600;700&family=Playfair+Display:wght@700;900&family=Rye&display=swap">
<style>
  :root {
    --chalk-dark: #2f2f31;
    --chalk-mid: #4a4b4d;
    --title-red: #c8161d;
    --accent-orange: #f2a81d;
    --accent-yellow: #f7b21b;
    --navy: #1c3442;
    --text-grey: #4a4a4a;
    --box-border: #1c3442;
    --white: #ffffff;
  }
  * { box-sizing: border-box; margin: 0; padding: 0; }
  html, body { width: 927px; height: 1200px; overflow: hidden; background: var(--white); }
  body { font-family: "Open Sans", Arial, sans-serif; }

  .flyer { position: relative; width: 927px; height: 1200px; overflow: hidden; background: var(--white); }

  /* Hero */
  .hero-backdrop {
    position: absolute; left: 0; top: 0; width: 927px; height: 560px;
    background: radial-gradient(ellipse at 45% 40%, var(--chalk-mid) 0%, var(--chalk-dark) 75%);
  }
  .hero-photo {
    position: absolute; left: 534px; top: 50px; width: 330px; height: 500px;
    background: linear-gradient(180deg, #5b5b5d 0%, #8c7f76 45%, #d9d4cf 100%);
    border-radius: 160px 160px 0 0;
  }
  .hero-curve { position: absolute; left: 0; top: 470px; width: 927px; height: 110px; }

  .brand {
    position: absolute; left: 190px; top: 40px;
    display: flex; align-items: center; gap: 8px; white-space: nowrap;
    color: var(--white); font-family: "Open Sans", Arial, sans-serif; font-weight: 700; font-size: 17px;
  }
  .brand-mark { width: 22px; height: 22px; background: var(--title-red); flex: none; }

  .title {
    position: absolute; left: 50px; top: 130px; width: 470px; text-align: center;
    font-family: "Playfair Display", Georgia, serif; font-weight: 900;
    color: var(--title-red); font-size: 88px; line-height: 1.1;
    letter-spacing: -1px;
  }
  .tagline {
    position: absolute; left: 150px; top: 326px; width: 270px; text-align: center;
    font-family: "Rye", Georgia, serif; color: var(--white); line-height: 0.95;
  }
  .tagline .line-rock { font-size: 66px; display: block; }
  .tagline .line-the { font-size: 36px; display: block; }
  .tagline .line-test { font-size: 72px; display: block; }
  .success-badge { position: absolute; left: 448px; top: 418px; width: 106px; height: 106px; }

  /* Program info */
  .program { position: absolute; left: 66px; top: 572px; width: 840px; }
  .program-heading { color: var(--accent-orange); font-weight: 700; font-size: 23px; margin-bottom: 2px; white-space: nowrap; }
  .program-list { list-style: none; color: var(--text-grey); font-size: 19.5px; line-height: 33px; white-space: nowrap; }

  .highlights-label {
    position: absolute; left: 305px; top: 722px; width: 318px; height: 36px;
    background: var(--accent-orange); color: var(--white); border-radius: 18px;
    font-size: 22px; font-weight: 600; text-align: center; line-height: 36px;
  }
  .highlights { position: absolute; left: 68px; top: 768px; width: 782px; list-style: none; }
  .highlights li {
    height: 34px; margin-bottom: 6.4px; border: 2px solid var(--box-border); border-radius: 14px;
    display: flex; align-items: center; gap: 12px; padding-left: 20px; white-space: nowrap;
    color: var(--text-grey); font-size: 19px; background: var(--white);
  }
  .tick { width: 22px; height: 22px; flex: none; }

  /* Footer */
  .footer-shape { position: absolute; left: 0; top: 990px; width: 927px; height: 210px; }
  .phone { position: absolute; left: 44px; top: 1144px; display: flex; align-items: center; gap: 14px;
    color: var(--navy); font-weight: 700; font-size: 34px; }
  .phone svg { width: 38px; height: 38px; }
  .address { position: absolute; right: 47px; top: 1134px; text-align: right; color: var(--navy);
    font-size: 17px; line-height: 25px; font-style: normal; white-space: nowrap; }
  .address .web { font-weight: 700; }
  .social { position: absolute; top: 1085px; width: 40px; height: 40px; border-radius: 50%; background: var(--navy); }
  .social-a { left: 779px; }
  .social-b { left: 840px; }
</style>
</head>
<body>
<main class="flyer">
  <div class="hero-backdrop" role="img" aria-label="Chalkboard background with chalk doodles of stars, planets and a rocket"></div>
  <div class="hero-photo" role="img" aria-label="Photo of a smiling young student raising her fist, with a chalk astronaut suit drawn around her"></div>

  <svg class="hero-curve" viewBox="0 0 927 110" preserveAspectRatio="none" aria-hidden="true">
    <path d="M0 70 Q 470 20 927 30 L927 110 L0 110 Z" fill="var(--accent-yellow)"/>
    <path d="M0 84 Q 470 36 927 44 L927 110 L0 110 Z" fill="var(--white)"/>
  </svg>

  <div class="brand"><span class="brand-mark"></span>Brightpath Learning</div>

  <h1 class="title">Georgia Milestones</h1>
  <p class="tagline"><span class="line-rock">ROCK</span><span class="line-the">THE</span><span class="line-test">TEST</span></p>
  <svg class="success-badge" viewBox="0 0 106 106" aria-hidden="true">
    <circle cx="53" cy="53" r="50" fill="var(--title-red)"/>
    <circle cx="53" cy="53" r="38" fill="var(--white)"/>
  </svg>

  <section class="program">
    <h2 class="program-heading">Comprehensive students assessment program spanning grades 3-12</h2>
    <ul class="program-list">
      <li>- Grade 3 through 8 take an end-of-grade assessment in Language Arts and Mathematics</li>
      <li>- Grade 5 and 8 are also assessed in Science and Social Studies</li>
      <li>- High school students take an end-of-course assessment (EOC)</li>
    </ul>
  </section>

  <h2 class="highlights-label">COURSE HIGHLIGHTS</h2>
  <ul class="highlights">
    <li><svg class="tick" viewBox="0 0 22 22" aria-hidden="true"><circle cx="11" cy="11" r="9" fill="none" stroke="var(--accent-orange)" stroke-width="2"/><path d="M6.5 11.5l3 3 6-6" fill="none" stroke="var(--accent-orange)" stroke-width="2.2"/></svg>Two hours coaching (Language &amp; Math) every weekend</li>
    <li><svg class="tick" viewBox="0 0 22 22" aria-hidden="true"><circle cx="11" cy="11" r="9" fill="none" stroke="var(--accent-orange)" stroke-width="2"/><path d="M6.5 11.5l3 3 6-6" fill="none" stroke="var(--accent-orange)" stroke-width="2.2"/></svg>Additional one-hour coaching in Science and Social Studies (Grade 5 and 8 only)</li>
    <li><svg class="tick" viewBox="0 0 22 22" aria-hidden="true"><circle cx="11" cy="11" r="9" fill="none" stroke="var(--accent-orange)" stroke-width="2"/><path d="M6.5 11.5l3 3 6-6" fill="none" stroke="var(--accent-orange)" stroke-width="2.2"/></svg>Course begins in January and ends in April</li>
    <li><svg class="tick" viewBox="0 0 22 22" aria-hidden="true"><circle cx="11" cy="11" r="9" fill="none" stroke="var(--accent-orange)" stroke-width="2"/><path d="M6.5 11.5l3 3 6-6" fill="none" stroke="var(--accent-orange)" stroke-width="2.2"/></svg>Classes conducted by certified and experienced school teachers</li>
    <li><svg class="tick" viewBox="0 0 22 22" aria-hidden="true"><circle cx="11" cy="11" r="9" fill="none" stroke="var(--accent-orange)" stroke-width="2"/><path d="M6.5 11.5l3 3 6-6" fill="none" stroke="var(--accent-orange)" stroke-width="2.2"/></svg>Pre and post assessment to identify and resolve skill gaps</li>
    <li><svg class="tick" viewBox="0 0 22 22" aria-hidden="true"><circle cx="11" cy="11" r="9" fill="none" stroke="var(--accent-orange)" stroke-width="2"/><path d="M6.5 11.5l3 3 6-6" fill="none" stroke="var(--accent-orange)" stroke-width="2.2"/></svg>Online practice and skill checkpoints</li>
    <li><svg class="tick" viewBox="0 0 22 22" aria-hidden="true"><circle cx="11" cy="11" r="9" fill="none" stroke="var(--accent-orange)" stroke-width="2"/><path d="M6.5 11.5l3 3 6-6" fill="none" stroke="var(--accent-orange)" stroke-width="2.2"/></svg>Revise and practice full year syllabus to boost student confidence</li>
    <li><svg class="tick" viewBox="0 0 22 22" aria-hidden="true"><circle cx="11" cy="11" r="9" fill="none" stroke="var(--accent-orange)" stroke-width="2"/><path d="M6.5 11.5l3 3 6-6" fill="none" stroke="var(--accent-orange)" stroke-width="2.2"/></svg>Use industry-proven test preparation materials</li>
  </ul>

  <svg class="footer-shape" viewBox="0 0 927 210" preserveAspectRatio="none" aria-hidden="true">
    <path d="M0 110 L927 110 L927 210 L0 210 Z" fill="var(--accent-yellow)"/>
    <path d="M360 112 Q 700 80 927 0 L927 20 Q 700 96 420 112 Z" fill="var(--navy)"/>
    <path d="M560 112 Q 780 80 927 38 L927 112 Z" fill="var(--white)"/>
  </svg>

  <span class="social social-a" aria-hidden="true"></span>
  <span class="social social-b" aria-hidden="true"></span>

  <div class="phone">
    <svg viewBox="0 0 38 38" aria-hidden="true"><circle cx="19" cy="19" r="16.5" fill="none" stroke="var(--navy)" stroke-width="3"/><path d="M13 11c1-1 2.2-1 3 .2l1.6 2.6c.5.9.3 1.8-.5 2.4l-1 .8c.9 2 2.5 3.7 4.6 4.7l.8-1c.6-.8 1.6-1 2.4-.5l2.6 1.6c1.2.8 1.2 2 .2 3l-1.4 1.4c-1.3 1.3-3.6 1-6.6-1-2.8-1.9-5-4.3-6.6-7.2-1.6-2.9-1.6-5.2-.3-6.4z" fill="var(--navy)"/></svg>
    678-555-0142
  </div>
  <address class="address">
    4215 Maple Ridge Rd, Suite 210 Suwanee, GA 30024<br>
    <span class="web">brightpathlearnga.example</span>
  </address>
</main>
</body>
</html>
```